Business card - house cleaning company

We want friendly high end business card highlighting our services . NO LOGOs on back of card please.. no vertical cards NO DOUBLE BROOMS

2 owners of the company: Corinne Halvey & Joel Brandt

Included phone number: (555)318-2047

Email: brightlanetidy@mailnest.example

Website: www.brightlanetidy.example

Bonded & Insured

Pine Hollow, CO 80599

Slogan maybe: Bringing a brighter shine to every corner of home

We want elegant high end card for house cleaning service. Maybe 2 sided if needed. Can it have bullet points of some services we offer

Residential Home Cleaning
Vacation Rental Cleaning
Commercial Cleaning
Carpet Cleaning
Window Cleaning
Property Management
Property Inspections
Property Maintenance
Trash Removal
Concierge Services

Highlight service on back of card. If we can do a one sided card with all this that’s great as well. Not cartoony.

Our logo attached and a design somone I had Perrin but they put very little time in. Not Unique enough. If you can do a custom design with a feminine touch that be great.

You will be eliminated for not reading the brief. NO DOUBLE LOGOS NO DOUBLE BROOMS. PLEASE BE CREATIVE. IF POST SAME LOGO WITH SMAL CHANGES RHEY WILL BE ELIMINATED. BE CREATIVE.

Thank you everyone for your designs. please only use the logo 1 time. and would love to see some that dont look all the same. We appreciate your time.

Target Market(s)

Residential and vacation rental home cleaning maid service

Industry/Entity Type

House cleaning maid services

Contact Information for Business Card

For business card use logo. black and green one provided. others for example. I wil try find some example.. We want friendly high end look. 2 owners of the company: Corinne Halvey & Joel Brandt Included phone number: (555)318-2047 Email: brightlanetidy@mailnest.example Website: www.brightlanetidy.example Bonded & Insured Estes Park, CO Slogan maybe: Bringing a brighter shine to every corner of home or Quality Service Guaranteed We want elegant high end card for house cleaning service. Maybe 2 sided if needed. Can it have bullet points of some services we offer Residential Home Cleaning Vacation Rental Cleaning Commercial Cleaning Carpet Cleaning Window Cleaning Property Management Property Inspections Property Maintenance Trash Removal Concierge Services

Requirements
Must have
• For business card use logo . Creativity. black and green one provided. We want friendly high end look. 2 owners of the company: Corinne Halvey & Joel Brandt Included phone number: (555)318-2047 Email: brightlanetidy@mailnest.example Website: www.brightlanetidy.example Licensed Bonded & Insured Estes Park, CO Slogan maybe: Bringing a brighter shine to every corner of home or Quality Service Guaranteed We want elegant high end card for house cleaning service. Maybe 2 sided if needed. Can it have bullet points of some services we offer Residential Home Cleaning Vacation Rental Cleaning Commercial Cleaning Carpet Cleaning Window Cleaning Property Management Property Inspections Property Maintenance Trash Removal Concierge Services .. creatitivty a plus. whimsical. we like stars..
Nice to have
• we want much better than the example of biz card provided as example. logo has colors that are in our website palette as well. We are open to ideas for the business card design. Will pay tip to best work. PLEASE USE COMPLIMENTING COLORS. . WE LIKE BLACK AND WHITE, stars
Should not have
• NO DOUBLE LOGOS. READ READ. READ. YOU WILL BE ELIMINATED no double logos or double brooms same side of card. I want didfrent examples. please don't make all your submission look the same

```html
<!DOCTYPE html>
<html lang="en">
<head>
<meta charset="utf-8">
<title>Brightlane Tidy Services – Business Card</title>
<link href="https://fonts.googleapis.com/css2?family=Lato:ital,wght@0,400;0,700;1,400;1,700&family=Lora:ital@1&display=swap" rel="stylesheet">
<style>
  :root{
    --ink:#1e1e1e;
    --green:#6b9a45;
    --paper:#ffffff;
    --night:#1b1b1b;
    --muted:#9b9b9b;
    --page:#ffffff;
  }
  *{box-sizing:border-box;margin:0;padding:0}
  html,body{width:1200px;height:1200px;overflow:hidden;background:var(--page)}
  body{position:relative;font-family:'Lato',sans-serif;color:var(--ink)}
  .card{position:absolute;left:241px;width:725px;height:414px;box-shadow:0 6px 22px rgba(0,0,0,.08);overflow:hidden}
  .card--front{top:143px;background:var(--paper)}
  .card--back{top:651px;background:var(--night)}

  .brand{position:absolute;left:28px;top:62px;display:flex;align-items:center;gap:12px}
  .brand__dot{width:16px;height:16px;border-radius:50%;background:var(--green)}
  .brand__name{font-weight:700;font-size:46px;letter-spacing:.5px;color:var(--ink);line-height:1}

  .owners{position:absolute;right:34px;top:222px;font-weight:700;font-size:22px;letter-spacing:.1px;text-transform:uppercase}
  .rule{position:absolute;left:38px;top:257px;width:585px;height:1.5px;background:var(--ink)}
  .role{position:absolute;right:34px;top:246px;color:var(--green);font-size:19px}

  .contact{position:absolute;left:40px;top:285px;list-style:none}
  .contact li{display:flex;align-items:center;height:28.7px;font-size:19px}
  .contact svg{width:16px;height:16px;margin-right:11px;fill:var(--green)}

  .location{position:absolute;right:61px;top:285px;text-align:right;font-size:19px}
  .location__line{height:28.7px;display:flex;align-items:center;justify-content:flex-end;white-space:nowrap}
  .location__line svg{width:14px;height:19px;margin-left:11px;margin-right:-25px;fill:none;stroke:var(--green);stroke-width:2.2}
  .location__cred{font-style:italic}

  .tagline{position:absolute;left:0;bottom:0;width:520px;height:39px}
  .tagline svg{position:absolute;inset:0;width:100%;height:100%}
  .tagline__text{position:absolute;left:36px;top:0;line-height:39px;font-family:'Lora',serif;font-style:italic;font-size:20px;color:#fff;white-space:nowrap}

  .services{position:absolute;right:52px;top:35px;list-style:none;text-align:right}
  .services li{font-style:italic;font-weight:700;font-size:23px;color:var(--muted);height:34.5px;line-height:34.5px;white-space:nowrap}
</style>
</head>
<body>
  <section class="card card--front">
    <div class="brand">
      <span class="brand__dot"></span>
      <span class="brand__name">Brightlane Tidy Services</span>
    </div>

    <p class="owners">Corinne Halvey &amp; Joel Brandt</p>
    <div class="rule"></div>
    <p class="role">Owner</p>

    <ul class="contact">
      <li><svg viewBox="0 0 16 16"><path d="M1 6c0-2 3-3.5 7-3.5S15 4 15 6v1.2h-3.6V5.6c-1-.4-5.8-.4-6.8 0v1.6H1z"/><path d="M3.5 8.2h9l1.5 5.3H2z"/><circle cx="8" cy="10.6" r="1.3" fill="#fff"/></svg>(555) 318-2047</li>
      <li><svg viewBox="0 0 16 16"><path d="M1 3.5h14v9H1z"/><path d="M1 3.5l7 5.2 7-5.2" fill="none" stroke="#fff" stroke-width="1.2"/></svg>brightlanetidy@mailnest.example</li>
      <li><svg viewBox="0 0 16 16"><circle cx="8" cy="8" r="7"/><path d="M1 8h14M8 1v14M3 4h10M3 12h10" stroke="#fff" stroke-width=".9" fill="none"/><ellipse cx="8" cy="8" rx="3.2" ry="7" fill="none" stroke="#fff" stroke-width=".9"/></svg>www.brightlanetidy.example</li>
    </ul>

    <div class="location">
      <p class="location__line">Pine Hollow, CO 80599<svg viewBox="0 0 14 19"><path d="M7 17.5S1.5 11 1.5 7a5.5 5.5 0 0 1 11 0C12.5 11 7 17.5 7 17.5z"/><circle cx="7" cy="7" r="2"/></svg></p>
      <p class="location__line location__cred">Licensed Bonded &amp; Insured</p>
    </div>

    <div class="tagline">
      <svg viewBox="0 0 520 39" preserveAspectRatio="none"><path d="M0 0H493Q500 0 503 6L520 39H0z" fill="#1e1e1e"/></svg>
      <p class="tagline__text">Bringing a brighter shine to every corner of home</p>
    </div>
  </section>

  <section class="card card--back">
    <ul class="services">
      <li>Residential Home Cleaning</li>
      <li>Vacation Rental Cleaning</li>
      <li>Commercial Cleaning</li>
      <li>Carpet Cleaning</li>
      <li>Window Cleaning</li>
      <li>Property Management</li>
      <li>Property Inspections</li>
      <li>Property Maintenance</li>
      <li>Trash Removal</li>
      <li>Concierge Services</li>
    </ul>
  </section>
</body>
</html>
```